We are an online mail order nursery selling live plants who needs a 1 page landing page for an upcom

We are opening a new sister site to our main site. The new site is membership based. We need a landing page for an email campaign that is both attention grabbing and simply luring the customer to click on the learn more about Membership Page : http://www.thefernguild.com/pages/membership-info
The landing page will need to have space reserved for a white board presentation. I have attached the video below. The vid will be hosted on You tube so we should be able to use the iframe / embed technique. Again our goal is to funnel the customer to http://www.thefernguild.com/pages/membership-info where they can get more details.

Target Market(s)

Home owners between the age of 35 and 65 - gardening enthusiast

Industry/Entity Type

Campaign

Number of Pages Required

1 page

Font styles to use
Sans Serif

Requirements
Must have
• space to embed white board video

```html
<!DOCTYPE html>
<html lang="en">
<head>
<meta charset="utf-8">
<title>The Fern Guild – Membership</title>
<link rel="stylesheet" href="https://fonts.googleapis.com/css2?family=Raleway:ital,wght@0,400;0,500;0,600;0,700;1,400&family=Lato:wght@400;700&display=swap">
<style>
:root{
  --green:#8cc63f;
  --green-dark:#1f5e2a;
  --ink:#1e1e1e;
  --grey-text:#7a7a7a;
  --nav-text:#6b6b6b;
  --about-bg:#f5f5f5;
  --footer-bg:#e3e3e3;
  --social:#666666;
  --placeholder:#ececec;
  --white:#ffffff;
}
*{box-sizing:border-box;margin:0;padding:0}
html,body{width:1066px;height:1200px;overflow:hidden}
body{position:relative;background:var(--white);font-family:'Lato',sans-serif;color:var(--ink)}
a{text-decoration:none;color:inherit}

.top-rule,.bottom-rule{position:absolute;left:0;width:1066px;height:6px;background:var(--green)}
.top-rule{top:0}.bottom-rule{top:1194px}

.site-header{position:absolute;top:6px;left:0;width:1066px;height:72px}
.brand{position:absolute;left:134px;top:26px;display:flex;align-items:center;gap:10px}
.brand-dot{width:26px;height:26px;border-radius:50%;background:var(--green-dark)}
.brand-name{font-family:'Raleway',sans-serif;font-weight:600;font-size:20px;color:var(--green-dark);letter-spacing:.5px}
.main-nav{position:absolute;top:24px;left:550px;display:flex;align-items:center;font-family:'Raleway',sans-serif;font-weight:600;font-size:12.5px;color:var(--nav-text)}
.main-nav a{margin-right:31px}
.main-nav .btn-signup{margin:0 0 0 -11px;background:var(--green);color:var(--white);width:78px;height:30px;border-radius:3px;display:flex;align-items:center;justify-content:center}

.hero{position:absolute;top:78px;left:0;width:1066px;height:418px;text-align:center;color:var(--white)}
.hero-photo{position:absolute;inset:0;background:radial-gradient(ellipse at 20% 85%,#0f4a2a 0%,rgba(15,74,42,0) 45%),linear-gradient(120deg,#6fd23a 0%,#3aa83a 40%,#55c04a 75%,#6cc94e 100%)}
.hero-content{position:relative;padding-top:168px}
.hero h1{font-family:'Raleway',sans-serif;font-weight:700;font-size:32px;letter-spacing:3px}
.hero p{font-family:'Raleway',sans-serif;font-size:16px;letter-spacing:.8px;margin-top:13px}
.btn-outline-light{display:inline-block;margin-top:31px;width:119px;height:30px;line-height:26px;border:2px solid var(--white);border-radius:3px;font-family:'Raleway',sans-serif;font-weight:700;font-size:14px;letter-spacing:1px}

.about{position:absolute;top:496px;left:0;width:1066px;height:310px;background:var(--about-bg)}
.about h2{position:absolute;left:141px;top:56px;font-family:'Raleway',sans-serif;font-weight:600;font-size:14.5px}
.about-lead{position:absolute;left:140px;top:87px;width:345px;font-family:'Raleway',sans-serif;font-style:italic;font-size:16.4px;line-height:19px;color:var(--grey-text)}
.subscribe{position:absolute;left:140px;top:208px;display:flex;height:37px}
.subscribe-field{width:203px;border:1px solid #d6d6d6;border-right:none;border-radius:8px 0 0 8px;background:var(--white);padding-left:16px;display:flex;align-items:center;font-family:'Raleway',sans-serif;font-weight:500;font-size:12.5px;color:var(--grey-text)}
.subscribe-btn{width:94px;background:var(--green);color:var(--white);border-radius:0 8px 8px 0;display:flex;align-items:center;justify-content:center;font-family:'Raleway',sans-serif;font-weight:700;font-size:15px;letter-spacing:.5px}

.video-card{position:absolute;left:581px;top:46px;width:345px;height:212px;background:var(--white);border-radius:5px}
.video-poster{position:absolute;left:69px;top:22px;width:216px;height:140px;border-radius:4px;background:var(--placeholder)}
.video-controls{position:absolute;left:13px;top:168px;width:319px;height:30px}

.features{position:absolute;top:806px;left:0;width:1066px;height:300px}
.feature{position:absolute;top:31px;width:240px;text-align:center}
.feature:nth-child(1){left:131px}.feature:nth-child(2){left:414px}.feature:nth-child(3){left:697px}
.feature-icon{width:64px;height:64px;border-radius:50%;background:var(--green);margin:0 auto;display:flex;align-items:center;justify-content:center}
.feature h3{margin-top:20px;font-weight:400;font-size:14.5px;color:var(--ink)}
.feature p{width:236px;margin:11px auto 0;font-size:10.4px;line-height:17.2px;color:var(--grey-text)}
.btn-outline-green{display:inline-block;margin-top:8px;height:24px;padding:0 6px;line-height:20px;border:2px solid var(--green);border-radius:3px;font-size:9.5px;color:var(--ink)}

.site-footer{position:absolute;top:1106px;left:0;width:1066px;height:88px;background:var(--footer-bg)}
.copyright{position:absolute;left:140px;top:38px;font-family:'Raleway',sans-serif;font-weight:600;font-size:10.5px;color:#777;text-transform:uppercase}
.social{position:absolute;left:757px;top:32px;display:flex;gap:5.5px}
.social a{width:24px;height:24px;border-radius:50%;background:var(--social)}
.social a.is-active{background:var(--green)}
</style>
</head>
<body>
<div class="top-rule"></div>

<header class="site-header">
  <a class="brand" href="#"><span class="brand-dot"></span><span class="brand-name">THE FERN GUILD</span></a>
  <nav class="main-nav">
    <a href="#">Home</a>
    <a href="http://www.thefernguild.com/pages/membership-info">Membership</a>
    <a href="#">Contact US</a>
    <a class="btn-signup" href="http://www.thefernguild.com/pages/membership-info">Sign Up</a>
  </nav>
</header>

<section class="hero">
  <div class="hero-photo" role="img" aria-label="Close-up photo of a young green seedling against a soft blurred green background"></div>
  <div class="hero-content">
    <h1>WE GROW PLANTS</h1>
    <p>Beautiful, healty, affordable plants.</p>
    <a class="btn-outline-light" href="http://www.thefernguild.com/pages/membership-info">learn more</a>
  </div>
</section>

<section class="about">
  <h2>About Us</h2>
  <p class="about-lead">We decided to develop a method for cutting production cost and passing the savings along to our fellow gardeners. the results, we can provide plants at half the price that most mail order nursering sell thier plants for.</p>
  <form class="subscribe">
    <div class="subscribe-field">Email Address</div>
    <div class="subscribe-btn">Subscribe</div>
  </form>
  <div class="video-card">
    <div class="video-poster" role="img" aria-label="Video poster image for the membership presentation"></div>
    <svg class="video-controls" viewBox="0 0 319 30" aria-hidden="true">
      <rect x="0" y="0" width="53" height="30" rx="2" fill="#444"/>
      <path d="M21 8 L33 15 L21 22 Z" fill="#fff"/>
      <rect x="61" y="7" width="258" height="21" rx="2" fill="#444"/>
      <rect x="70" y="15" width="176" height="6" fill="#666"/>
      <rect x="70" y="15" width="112" height="6" fill="#1e9be0"/>
      <rect x="168" y="1" width="26" height="9" rx="1" fill="#fff"/>
      <text x="181" y="8.3" font-family="Lato,sans-serif" font-size="6.5" font-weight="700" text-anchor="middle" fill="#222">01:34</text>
      <g fill="#1e9be0"><rect x="252" y="13" width="1.3" height="9"/><rect x="255" y="13" width="1.3" height="9"/><rect x="258" y="13" width="1.3" height="9"/><rect x="261" y="13" width="1.3" height="9"/><rect x="264" y="13" width="1.3" height="9"/><rect x="267" y="13" width="1.3" height="9"/><rect x="270" y="13" width="1.3" height="9"/></g>
      <text x="276" y="21" font-family="Lato,sans-serif" font-size="9" font-style="italic" font-weight="700" fill="#1e9be0">HD</text>
      <path d="M300 13h3v1.5h-1.5V16H300zM308 13h3v3h-1.5v-1.5H308zM300 19h1.5v1.5H303V22h-3zM309.5 19H311v3h-3v-1.5h1.5z" fill="#fff"/>
    </svg>
  </div>
</section>

<section class="features">
  <article class="feature">
    <div class="feature-icon"><svg width="32" height="32" viewBox="0 0 32 32" aria-hidden="true"><rect x="3" y="14" width="6" height="14" rx="1" fill="#fff"/><path d="M11 14 L16 6 C17 3 21 4 20 8 L19 12 H27 C29 12 30 14 29 16 L26 26 C25.5 27.5 24.5 28 23 28 H11 Z" fill="#fff"/></svg></div>
    <h3>Satisfaction Guaranteed</h3>
    <p>We guarantee our plants to arrive in good, healthy condition labeled true to name. At the time of sale our plants are guaranteed to be free of known hosta viruses, foliar nematodes and disease free perennials . . . .</p>
    <a class="btn-outline-green" href="#">Learn more</a>
  </article>
  <article class="feature">
    <div class="feature-icon"><svg width="30" height="30" viewBox="0 0 30 30" aria-hidden="true"><path d="M15 2 L18.8 10.6 L28 11.4 L21 17.5 L23.1 26.6 L15 21.8 L6.9 26.6 L9 17.5 L2 11.4 L11.2 10.6 Z" fill="#fff"/></svg></div>
    <h3>Company History</h3>
    <p>We have been in the nursery business for 30 rears. We got into the mail order business in 2001. We operate one retail garden center and are in the process of constructing a second retail location. There is nothing to see at&nbsp; . . . .</p>
    <a class="btn-outline-green" href="#">Learn more</a>
  </article>
  <article class="feature">
    <div class="feature-icon"><svg width="34" height="34" viewBox="0 0 34 34" aria-hidden="true"><circle cx="17" cy="11" r="7" fill="#fff"/><path d="M4 31 C4 23 9 19 17 19 C25 19 30 23 30 31 Z" fill="#fff"/></svg></div>
    <h3>A Great Customer</h3>
    <p>Have you ever heard the expression "The more I get to know people the more I like my dog"....... if you feel like you fall into that description of people please don't order from us. Running a mail order . . . .</p>
    <a class="btn-outline-green" href="#">Learn more</a>
  </article>
</section>

<footer class="site-footer">
  <p class="copyright">Copyright © 2016 The Fern Guild | Powered by Cartwell</p>
  <nav class="social" aria-label="Social links">
    <a href="#" aria-label="Social link 1"></a>
    <a href="#" aria-label="Social link 2"></a>
    <a href="#" class="is-active" aria-label="Social link 3"></a>
    <a href="#" aria-label="Social link 4"></a>
    <a href="#" aria-label="Social link 5"></a>
    <a href="#" aria-label="Social link 6"></a>
  </nav>
</footer>

<div class="bottom-rule"></div>
</body>
</html>
```